MS Word Template needed for a company specialized in network and security infrastructures

We need a new MS Word Template. <br/>Our activity is services in IT (network infrastructure and security). We usually use french language. <br/>The template must be nice and beautiful, and easy to use. If possible, try to use as less as possible text zones to simplify redaction tasks. And try to use "native" polices in MS Word. I attached sample documents for example. Please try to use the same colour codes.

Target Market(s)

Consulting in Network and security domain

Industry/Entity Type

It Service

Colors

Designer to choose colors to be used in the design.

Requirements
Must have
• - Nice design
• - Easy to use
• - very professional aspect
Nice to have
• - actual ox relay solutions logo
• - actual colour code

```html
<!DOCTYPE html>
<html lang="fr">
<head>
<meta charset="utf-8">
<title>Ox Relay Solutions – Modèle de document</title>
<link rel="stylesheet" href="https://fonts.googleapis.com/css2?family=Montserrat:wght@700;800&family=Lato:wght@400;700&display=swap">
<style>
  :root {
    --teal-dark: #2f7b78;
    --teal: #3ec8a0;
    --green-mint: #4fe07a;
    --green: #5fdc3a;
    --green-lime: #7cd80a;
    --green-wave: #6fea5c;
    --teal-wave: #3dbcb0;
    --headline: #2d5a5e;
    --body-text: #3a3a3a;
    --contact: #1f2a5a;
    --grid: #d9d9d9;
    --axis-text: #777;
    --page: #ffffff;
  }
  * { margin: 0; padding: 0; box-sizing: border-box; }
  html, body { width: 847px; height: 1200px; overflow: hidden; background: var(--page); }
  .page { position: relative; width: 847px; height: 1200px; overflow: hidden; background: var(--page); font-family: "Lato", Arial, sans-serif; }

  .brand { position: absolute; left: 119px; top: 66px; display: flex; align-items: center; gap: 22px; }
  .brand-dot { width: 94px; height: 94px; border-radius: 50%; background: var(--teal); }
  .brand-name { font-family: "Lato", Arial, sans-serif; font-weight: 700; font-size: 25px; line-height: 1.1; color: var(--teal); letter-spacing: 1px; text-transform: uppercase; }

  .header-shadow { position: absolute; left: 0; top: 236px; width: 847px; height: 30px;
    background: radial-gradient(ellipse 55% 100% at 50% 0%, rgba(0,0,0,0.07), rgba(0,0,0,0) 70%); }

  .headline { position: absolute; left: 119px; top: 324px; font-family: "Montserrat", Arial, sans-serif; font-weight: 800; font-size: 28px; color: var(--headline); letter-spacing: 0.5px; }

  .body-copy { position: absolute; left: 119px; width: 263px; font-size: 14.6px; line-height: 17.6px; color: var(--body-text); text-align: justify; hyphens: manual; }
  .body-copy.first { top: 404px; }
  .body-copy.second { top: 690px; }

  .pie { position: absolute; left: 513px; top: 406px; }
  .pie text { font-family: "Lato", Arial, sans-serif; font-weight: 700; font-size: 18px; fill: #fff; text-anchor: middle; dominant-baseline: middle; }

  .bar-chart { position: absolute; left: 440px; top: 700px; }
  .bar-chart text { font-family: "Lato", Arial, sans-serif; font-size: 7.5px; fill: var(--axis-text); }

  .contact { position: absolute; left: 119px; top: 918px; font-size: 15.5px; color: var(--contact); line-height: 19px; }
  .contact .contact-title { margin-bottom: 0; }
  .contact .contact-name { margin-bottom: 23px; }

  .footer-waves { position: absolute; left: 0; top: 0; }
</style>
</head>
<body>
<div class="page">
  <svg class="footer-waves" width="847" height="1200" viewBox="0 0 847 1200" aria-hidden="true">
    <path d="M0,1200 L281,1080 L545,1134 L545,1200 Z" fill="var(--teal-wave)"/>
    <path d="M0,1200 C220,1176 520,1150 690,1055 C785,1000 832,930 847,862 L847,1200 Z" fill="var(--green-wave)"/>
  </svg>

  <div class="brand">
    <span class="brand-dot"></span>
    <span class="brand-name">Ox Relay<br>Solutions</span>
  </div>

  <div class="header-shadow"></div>

  <h1 class="headline">SUBJECT HEALINE HERE</h1>

  <p class="body-copy first">Lorem ipsum dolor sit amet, consectetur adipiscing elit. Donec diam nisi, sodales eu condimentum eget, blandit ac ex. Nunc sit amet diam lacinia sem finibus suscipit. Nunc con­sectetur euismod turpis, quis porttitor massa lobortis eget. Integer mollis sed lectus et pell. Quisque et pellentesque arcu.</p>

  <svg class="pie" width="200" height="200" viewBox="-100 -100 200 200" role="img" aria-label="Répartition en camembert : 8 %, 25 %, 20 %, 15 %, 12 %, 20 %">
    <path d="M0,0 L0,-98 A98,98 0 0 1 47.2,-85.9 Z" fill="var(--teal)"/>
    <path d="M0,0 L47.2,-85.9 A98,98 0 0 1 85.9,47.2 Z" fill="var(--green-mint)"/>
    <path d="M0,0 L85.9,47.2 A98,98 0 0 1 -18.4,96.3 Z" fill="#49e25c"/>
    <path d="M0,0 L-18.4,96.3 A98,98 0 0 1 -88.7,41.7 Z" fill="var(--green)"/>
    <path d="M0,0 L-88.7,41.7 A98,98 0 0 1 -93.2,-30.3 Z" fill="var(--green-lime)"/>
    <path d="M0,0 L-93.2,-30.3 A98,98 0 0 1 0,-98 Z" fill="var(--teal-dark)"/>
    <text x="9" y="-46">8%</text>
    <text x="47" y="-14">25%</text>
    <text x="21" y="47">20%</text>
    <text x="-32" y="42">15%</text>
    <text x="-50" y="3">12%</text>
    <text x="-30" y="-42">20%</text>
  </svg>

  <p class="body-copy second">Lorem ipsum dolor sit amet, consectetur adipiscing elit. Donec diam nisi, sodales eu condimentum eget, blandit ac ex. Nunc sit amet diam lacinia sem finibus suscipit. Nunc con­sectetur euismod turpis, quis porttitor massa lobortis eget. Integer mollis sed lectus et pel­lentesque. Proin volutpat augue quis eros tristique blandit. Quis­que et pellentesque arcu. Ves­tibulum eget lacus sollicitudin, suscipit fermentum. Curabi­tur quis nunc odio.</p>

  <svg class="bar-chart" width="350" height="245" viewBox="0 0 350 245" role="img" aria-label="Histogramme empilé à 100 % : quatre catégories, quatre séries">
    <g stroke="var(--grid)" stroke-width="0.8">
      <line x1="30" y1="29" x2="330" y2="29"/><line x1="30" y1="44.7" x2="330" y2="44.7"/>
      <line x1="30" y1="60.4" x2="330" y2="60.4"/><line x1="30" y1="76.1" x2="330" y2="76.1"/>
      <line x1="30" y1="91.8" x2="330" y2="91.8"/><line x1="30" y1="107.5" x2="330" y2="107.5"/>
      <line x1="30" y1="123.2" x2="330" y2="123.2"/><line x1="30" y1="138.9" x2="330" y2="138.9"/>
      <line x1="30" y1="154.6" x2="330" y2="154.6"/><line x1="30" y1="170.3" x2="330" y2="170.3"/>
      <line x1="30" y1="186" x2="330" y2="186"/>
      <line x1="30" y1="186" x2="14" y2="200"/><line x1="330" y1="186" x2="316" y2="200"/>
      <line x1="14" y1="200" x2="316" y2="200"/><line x1="330" y1="186" x2="346" y2="174"/>
    </g>
    <g text-anchor="end">
      <text x="24" y="31">100%</text><text x="24" y="47">90%</text><text x="24" y="62">80%</text>
      <text x="24" y="78">70%</text><text x="24" y="94">60%</text><text x="24" y="109">50%</text>
      <text x="24" y="125">40%</text><text x="24" y="141">30%</text><text x="24" y="156">20%</text>
      <text x="24" y="172">10%</text><text x="24" y="188">0%</text>
    </g>
    <!-- bars: front face + right side + top; plot 0%=186, 100%=29, 1%=1.57 -->
    <g>
      <rect x="76" y="115.4" width="26" height="70.6" fill="var(--teal-dark)"/>
      <rect x="76" y="80.8" width="26" height="34.6" fill="#3fb07a"/>
      <rect x="76" y="57.3" width="26" height="23.5" fill="var(--green-mint)"/>
      <rect x="76" y="29" width="26" height="28.3" fill="var(--green-wave)"/>
      <polygon points="102,29 109,23 109,180 102,186" fill="#1f5e5b"/>
      <polygon points="76,29 83,23 109,23 102,29" fill="#3fd23a"/>

      <rect x="142" y="143.6" width="26" height="42.4" fill="var(--teal-dark)"/>
      <rect x="142" y="77.7" width="26" height="65.9" fill="#3fb07a"/>
      <rect x="142" y="58.8" width="26" height="18.9" fill="var(--green-mint)"/>
      <rect x="142" y="29" width="26" height="29.8" fill="var(--green-wave)"/>
      <polygon points="168,29 175,23 175,180 168,186" fill="#1f5e5b"/>
      <polygon points="142,29 149,23 175,23 168,29" fill="#3fd23a"/>

      <rect x="208" y="129.5" width="26" height="56.5" fill="var(--teal-dark)"/>
      <rect x="208" y="104.4" width="26" height="25.1" fill="#3fb07a"/>
      <rect x="208" y="73" width="26" height="31.4" fill="var(--green-mint)"/>
      <rect x="208" y="29" width="26" height="44" fill="var(--green-wave)"/>
      <polygon points="234,29 241,23 241,180 234,186" fill="#1f5e5b"/>
      <polygon points="208,29 215,23 241,23 234,29" fill="#3fd23a"/>

      <rect x="274" y="137.3" width="26" height="48.7" fill="var(--teal-dark)"/>
      <rect x="274" y="112.2" width="26" height="25.1" fill="#3fb07a"/>
      <rect x="274" y="69.8" width="26" height="42.4" fill="var(--green-mint)"/>
      <rect x="274" y="29" width="26" height="40.8" fill="var(--green-wave)"/>
      <polygon points="300,29 307,23 307,180 300,186" fill="#1f5e5b"/>
      <polygon points="274,29 281,23 307,23 300,29" fill="#3fd23a"/>
    </g>
    <g text-anchor="middle">
      <text x="86" y="212">Category 1</text><text x="152" y="212">Category 2</text>
      <text x="218" y="212">Category 3</text><text x="284" y="212">Category 4</text>
    </g>
    <g>
      <rect x="70" y="230" width="6" height="6" fill="var(--teal-dark)"/><text x="80" y="236">Series 1</text>
      <rect x="124" y="230" width="6" height="6" fill="#3fb07a"/><text x="134" y="236">Series 2</text>
      <rect x="178" y="230" width="6" height="6" fill="var(--green-mint)"/><text x="188" y="236">Series 3</text>
      <rect x="232" y="230" width="6" height="6" fill="var(--green-wave)"/><text x="242" y="236">Series 4</text>
    </g>
  </svg>

  <div class="contact">
    <p class="contact-title">Nous contacter :</p>
    <p class="contact-name">Mathis CORVELL / Directeur</p>
    <p class="contact-email">mathis.corvell@oxrelaysolutions.fr</p>
    <p class="contact-phone">06 41 72 18 90</p>
  </div>
</div>
</body>
</html>
```